Book jacket for Harrowby

We need a book jacket design (hard cover front, back, spine, flaps; soft cover and eBook). for a social psychology book with the general cluelessness (being "out of it") of how people function both in their personal and social lives. This is the third book written by the author, a practicing psychiatrist, and the content centers on a single subject, people's lack of genuine emotional contact, their cluelessness with themselves and with current national and world events.
Updates

Need extra days to review

Target Market(s)

People who want to better understand the state the nation and world is in now, and what they can do about it.

Font styles to use
Serif
Sans Serif

Requirements
Must have
• Bold, eye-catching cover
Nice to have
• Like the idea of separating the title word (harrow by) to better emphasize the concept of lack of contact

```html
<!DOCTYPE html>
<html lang="en">
<head>
<meta charset="utf-8">
<title>Harrowby – Book Cover</title>
<link rel="stylesheet" href="https://fonts.googleapis.com/css2?family=Cinzel:wght@500;700&display=swap">
<style>
  :root {
    --stage: #8a8a8a;
    --paper: #ffffff;
    --ink: #0d0d0d;
    --ink-soft: #3a3a3a;
    --art-warm: #f47b20;
    --art-mid: #f2c14e;
    --art-cool: #1e9bd7;
    --art-violet: #6a3d9a;
  }
  html, body {
    margin: 0;
    width: 1200px;
    height: 800px;
    overflow: hidden;
    background: var(--stage);
  }
  .stage {
    width: 1200px;
    height: 800px;
    display: flex;
    align-items: center;
    justify-content: center;
  }
  .cover {
    width: 480px;
    height: 720px;
    background: var(--paper);
    box-sizing: border-box;
    display: flex;
    flex-direction: column;
    align-items: center;
    padding: 72px 32px 52px;
  }
  .cover__title {
    margin: 0;
    font-family: "Cinzel", "Times New Roman", serif;
    font-weight: 700;
    font-size: 64px;
    line-height: 1;
    letter-spacing: 0.01em;
    color: var(--ink);
    white-space: nowrap;
  }
  .cover__title-tail {
    color: var(--ink-soft);
  }
  .cover__art {
    width: 320px;
    height: 380px;
    margin-top: 64px;
    border-radius: 50% 50% 46% 46%;
    background: radial-gradient(circle at 50% 42%,
      var(--paper) 0 6%,
      var(--art-mid) 18%,
      var(--art-warm) 38%,
      var(--art-cool) 62%,
      var(--art-violet) 80%,
      var(--paper) 100%);
  }
  .cover__author {
    margin: auto 0 0;
    font-family: "Cinzel", "Times New Roman", serif;
    font-weight: 500;
    font-size: 26px;
    letter-spacing: 0.02em;
    color: var(--ink);
    white-space: nowrap;
  }
</style>
</head>
<body>
  <main class="stage">
    <section class="cover">
      <h1 class="cover__title">HARROW<span class="cover__title-tail">BY</span></h1>
      <div class="cover__art" role="img" aria-label="Cover illustration in bright rainbow tones"></div>
      <p class="cover__author">Daniel Morrow M.D.</p>
    </section>
  </main>
</body>
</html>
```